Carpet Cleaning Door Hanger Design Project

please design a door hanger for us. we do carpet cleaning. our company name is Velta Rug Works. our telephone number is 866-402-5719.

please make a special offer coupon.

please add bullets containing the following info-
Professional carpet, hardwood, tile & grout deep steam cleaning.
kid & pet safe.
fast drying.
100% eco friendly / toxin free products.
pet stain/s & odor control.
same day appointments.
clean uniformed employees.
and please put few other catchy lines.

please make a $20.00 of carpet cleaning coupon (restrictions apply).
please make a rooms starting at $59.99 (restrictions apply).

please also put- when you want the best for less call velta rug works.

Target Market(s)

home owners, home renters. new home buyers. new home sellers.

Industry/Entity Type

Home Improvement

Requirements
Must have
• special offer.
• double sided.
• must be a design for a door hanger.
Nice to have
• 100% satisfaction guaranteed bubble.
Should not have
• no website please

```html
<!DOCTYPE html>
<html lang="en">
<head>
<meta charset="utf-8">
<title>Velta Rug Works – Door Hanger</title>
<link rel="stylesheet" href="https://fonts.googleapis.com/css2?family=Open+Sans:wght@300;400;600;700;800&family=Oswald:wght@500;600&display=swap">
<style>
  :root {
    --backdrop: #e6e6e4;
    --white: #ffffff;
    --navy: #1b3a93;
    --royal: #1f56b3;
    --deep: #163584;
    --cyan: #3cc6f2;
    --sky: #29a9e1;
    --yellow: #f9d015;
    --gold: #f5b81c;
    --ink: #111111;
    --dots: #5aa845;
  }
  * { box-sizing: border-box; margin: 0; padding: 0; }
  html, body { width: 1179px; height: 1200px; overflow: hidden; }
  body {
    background: var(--backdrop);
    position: relative;
    font-family: "Open Sans", Arial, sans-serif;
  }
  .hanger {
    position: absolute;
    top: 80px;
    width: 430px;
    height: 1050px;
    overflow: hidden;
    box-shadow: 0 6px 18px rgba(0,0,0,.18);
  }
  .hanger--front { left: 121px; }
  .hanger--back { left: 630px; }
  .hanger__art { position: absolute; inset: 0; width: 430px; height: 1050px; }
  .brand-title {
    position: absolute; top: 10px; left: 0; width: 100%;
    text-align: center; font-weight: 700; font-size: 30px;
    letter-spacing: .5px; color: var(--sky);
  }
  .service-pill {
    position: absolute; left: 16px; top: 408px; width: 402px; height: 44px;
    border-radius: 22px; background: var(--yellow);
    display: flex; align-items: center; justify-content: center;
    font-weight: 700; font-size: 22px; color: var(--navy);
    box-shadow: 0 2px 4px rgba(0,0,0,.25);
  }
  .intro {
    position: absolute; top: 460px; left: 0; width: 100%;
    text-align: center; color: var(--white); font-size: 18px; line-height: 25px;
  }
  .intro strong { color: var(--yellow); font-weight: 700; }
  .checkbox { position: absolute; width: 52px; height: 48px; }
  .coupon__label {
    position: absolute; left: 78px; font-weight: 700; font-size: 25px;
    color: var(--ink); letter-spacing: .3px;
  }
  .coupon__price {
    position: absolute; font-family: "Oswald", "Arial Narrow", sans-serif;
    font-weight: 600; color: var(--navy); line-height: 1;
  }
  .coupon__from {
    position: absolute; left: 81px; top: 828px;
    font-family: "Oswald", "Arial Narrow", sans-serif; font-weight: 500;
    font-size: 21px; line-height: 23px; color: var(--navy);
  }
  .coupon__note { position: absolute; left: 73px; font-size: 15px; color: var(--ink); }
  .footer-brand {
    position: absolute; right: 10px; top: 937px;
    font-size: 24px; font-weight: 400; color: var(--yellow);
  }
  .footer-tagline {
    position: absolute; right: 10px; top: 969px; text-align: right;
    font-size: 14.5px; line-height: 19px; font-weight: 600; color: var(--white);
  }
  .footer-phone {
    position: absolute; right: 10px; top: 1007px;
    display: flex; align-items: center; gap: 8px;
    font-size: 30px; font-weight: 800; color: var(--yellow);
  }
  .footer-phone svg { width: 32px; height: 32px; }
  .back-heading {
    position: absolute; top: 468px; left: 0; width: 100%;
    text-align: center; font-size: 21px; line-height: 29px;
    font-weight: 700; color: var(--yellow);
  }
  .benefits { position: absolute; top: 546px; left: 13px; list-style: none; }
  .benefits li {
    height: 41px; display: flex; align-items: center; gap: 14px;
    font-size: 20px; font-weight: 600; color: var(--white);
  }
  .benefits svg { width: 30px; height: 30px; flex: none; }
</style>
</head>
<body>

<!-- Front side -->
<section class="hanger hanger--front">
  <svg class="hanger__art" viewBox="0 0 430 1050">
    <defs>
      <linearGradient id="frontBlue" x1="0" y1="0" x2="1" y2="1">
        <stop offset="0" stop-color="#1a3f9a"/>
        <stop offset="1" stop-color="#1f5fc0"/>
      </linearGradient>
      <linearGradient id="frontPhoto" x1="0" y1="0" x2="1" y2="1">
        <stop offset="0" stop-color="#eceff2"/>
        <stop offset=".55" stop-color="#e9ddd3"/>
        <stop offset="1" stop-color="#f3f3f3"/>
      </linearGradient>
      <radialGradient id="seal" cx=".4" cy=".35" r=".7">
        <stop offset="0" stop-color="#ffe28a"/>
        <stop offset="1" stop-color="#d99a14"/>
      </radialGradient>
    </defs>
    <rect width="430" height="1050" fill="#fff"/>
    <path role="img" aria-label="Photo of a smiling child and a small dog lying on a soft white carpet" d="M0 68H430V380C380 335 320 318 250 322C160 328 70 345 0 320Z" fill="url(#frontPhoto)"/>
    <path d="M0 318C70 343 160 326 250 320C320 316 380 334 430 380V470H0Z" fill="var(--cyan)"/>
    <path d="M0 338C80 362 170 340 255 336C330 333 390 356 430 398V560C360 545 290 560 225 585C150 612 60 605 0 560Z" fill="url(#frontBlue)"/>
    <path d="M0 560C60 605 150 612 225 585C290 560 360 545 430 560V585C360 572 295 588 230 610C150 638 60 630 0 585Z" fill="var(--cyan)"/>
    <circle role="img" aria-label="Photo of a vacuum head on carpet" cx="377" cy="636" r="45" fill="#8a7f73" stroke="#fff" stroke-width="3"/>
    <circle role="img" aria-label="Photo of an upholstery wand cleaning a sofa" cx="377" cy="813" r="45" fill="#a7a9ad" stroke="#fff" stroke-width="3"/>
    <line x1="0" y1="761" x2="430" y2="761" stroke="var(--dots)" stroke-width="2" stroke-dasharray="2 3"/>
    <path d="M0 922C120 900 250 885 430 905V1050H0Z" fill="var(--cyan)"/>
    <path d="M0 940C120 918 250 905 430 922V1050H0Z" fill="url(#frontBlue)"/>
    <circle role="img" aria-label="Eco friendly badge" cx="361" cy="108" r="34" fill="#3aa635"/>
    <circle cx="82" cy="970" r="58" fill="url(#seal)" stroke="#f6d36a" stroke-width="4"/>
    <circle cx="82" cy="970" r="42" fill="none" stroke="#b27a0c" stroke-width="2"/>
    <line x1="0" y1="126" x2="140" y2="126" stroke="#666" stroke-width="1"/>
    <circle cx="212" cy="126" r="76" fill="var(--backdrop)"/>
  </svg>

  <h1 class="brand-title">VELTA RUG WORKS</h1>
  <div class="service-pill">CARPET &amp; UPHOLSTERY CLINING</div>
  <p class="intro">Professional carpet, hardwood, tile &amp;<br>grout deep steam cleaning.<br><strong>Call us for your FREE quote today!</strong></p>

  <svg class="checkbox" style="left:12px;top:628px" viewBox="0 0 52 48"><rect x="3" y="12" width="33" height="33" fill="#fff" stroke="var(--sky)" stroke-width="4"/><path d="M10 26L20 36L46 4" fill="none" stroke="var(--yellow)" stroke-width="7" stroke-linecap="round"/></svg>
  <div class="coupon__label" style="top:629px">CARPET CLEANING</div>
  <div class="coupon__price" style="left:76px;top:664px;font-size:58px">$20.00 OFF</div>
  <div class="coupon__note" style="top:722px">(restrictions apply)</div>

  <svg class="checkbox" style="left:12px;top:776px" viewBox="0 0 52 48"><rect x="3" y="12" width="33" height="33" fill="#fff" stroke="var(--sky)" stroke-width="4"/><path d="M10 26L20 36L46 4" fill="none" stroke="var(--yellow)" stroke-width="7" stroke-linecap="round"/></svg>
  <div class="coupon__label" style="top:786px">ROOMS CLEANING</div>
  <div class="coupon__from">ROOMS<br>STARTING AT</div>
  <div class="coupon__price" style="left:192px;top:818px;font-size:58px">$59.99</div>
  <div class="coupon__note" style="top:876px">(restrictions apply)</div>

  <div class="footer-brand">Velta Rug Works</div>
  <p class="footer-tagline">When you want the best for less<br>call velta rug works.</p>
  <div class="footer-phone">
    <svg viewBox="0 0 32 32"><circle cx="16" cy="16" r="14" fill="none" stroke="var(--yellow)" stroke-width="2.5"/><path d="M11 8l3 4-2 2c1 3 3 5 6 6l2-2 4 3-2 3c-7 0-13-6-13-13z" fill="var(--yellow)"/></svg>
    866-402-5719
  </div>
</section>

<!-- Back side -->
<section class="hanger hanger--back">
  <svg class="hanger__art" viewBox="0 0 430 1050">
    <defs>
      <linearGradient id="backBlue" x1="0" y1="0" x2="1" y2="1">
        <stop offset="0" stop-color="#1a3f9a"/>
        <stop offset="1" stop-color="#1f5fc0"/>
      </linearGradient>
      <linearGradient id="backPhoto" x1="0" y1="0" x2="1" y2="1">
        <stop offset="0" stop-color="#5b5e63"/>
        <stop offset=".5" stop-color="#b9b6b0"/>
        <stop offset="1" stop-color="#e4e2de"/>
      </linearGradient>
      <radialGradient id="sealBack" cx=".4" cy=".35" r=".7">
        <stop offset="0" stop-color="#ffe28a"/>
        <stop offset="1" stop-color="#d99a14"/>
      </radialGradient>
    </defs>
    <rect width="430" height="1050" fill="#fff"/>
    <path role="img" aria-label="Photo of a technician steam cleaning a beige carpet with a wand" d="M0 68H430V420C380 398 300 388 220 398C140 408 60 425 0 440Z" fill="url(#backPhoto)"/>
    <path d="M0 440C60 425 140 408 220 398C300 388 380 398 430 420V470C380 448 300 442 220 450C140 458 60 468 0 482Z" fill="var(--yellow)"/>
    <path d="M0 480C60 468 140 458 220 452C300 446 380 452 430 472V1050H0Z" fill="url(#backBlue)"/>
    <path d="M0 905C110 945 250 920 430 900V925C250 945 110 965 0 930Z" fill="var(--cyan)"/>
    <circle role="img" aria-label="Photo of a red wine stain on white carpet" cx="127" cy="842" r="45" fill="#e9e3e3" stroke="#fff" stroke-width="3"/>
    <circle role="img" aria-label="Photo of a rotary machine cleaning tile floor" cx="222" cy="842" r="47" fill="#9aa4ad" stroke="#fff" stroke-width="3"/>
    <circle role="img" aria-label="Photo of a spilled coffee cup on carpet" cx="315" cy="842" r="45" fill="#8c6a45" stroke="#fff" stroke-width="3"/>
    <circle role="img" aria-label="Eco friendly badge" cx="353" cy="218" r="34" fill="#3aa635"/>
    <circle cx="82" cy="970" r="58" fill="url(#sealBack)" stroke="#f6d36a" stroke-width="4"/>
    <circle cx="82" cy="970" r="42" fill="none" stroke="#b27a0c" stroke-width="2"/>
    <line x1="0" y1="126" x2="140" y2="126" stroke="#666" stroke-width="1"/>
    <circle cx="212" cy="126" r="76" fill="var(--backdrop)"/>
  </svg>

  <h1 class="brand-title">VELTA RUG WORKS</h1>
  <p class="back-heading">Professional carpet, hardwood, tile<br>&amp; grout deep steam cleaning.</p>
  <ul class="benefits">
    <li><svg viewBox="0 0 30 30"><rect x="2" y="7" width="21" height="21" fill="none" stroke="#fff" stroke-width="3"/><path d="M6 16l6 6L28 2" fill="none" stroke="var(--yellow)" stroke-width="5" stroke-linecap="round"/></svg>Kid &amp; pet safe</li>
    <li><svg viewBox="0 0 30 30"><rect x="2" y="7" width="21" height="21" fill="none" stroke="#fff" stroke-width="3"/><path d="M6 16l6 6L28 2" fill="none" stroke="var(--yellow)" stroke-width="5" stroke-linecap="round"/></svg>Fast drying</li>
    <li><svg viewBox="0 0 30 30"><rect x="2" y="7" width="21" height="21" fill="none" stroke="#fff" stroke-width="3"/><path d="M6 16l6 6L28 2" fill="none" stroke="var(--yellow)" stroke-width="5" stroke-linecap="round"/></svg>100% eco friendly/toxin free products</li>
    <li><svg viewBox="0 0 30 30"><rect x="2" y="7" width="21" height="21" fill="none" stroke="#fff" stroke-width="3"/><path d="M6 16l6 6L28 2" fill="none" stroke="var(--yellow)" stroke-width="5" stroke-linecap="round"/></svg>Pet stain/s &amp; odor control</li>
    <li><svg viewBox="0 0 30 30"><rect x="2" y="7" width="21" height="21" fill="none" stroke="#fff" stroke-width="3"/><path d="M6 16l6 6L28 2" fill="none" stroke="var(--yellow)" stroke-width="5" stroke-linecap="round"/></svg>Same day appointments</li>
    <li><svg viewBox="0 0 30 30"><rect x="2" y="7" width="21" height="21" fill="none" stroke="#fff" stroke-width="3"/><path d="M6 16l6 6L28 2" fill="none" stroke="var(--yellow)" stroke-width="5" stroke-linecap="round"/></svg>Clean uniformed employees</li>
  </ul>

  <div class="footer-brand">Velta Rug Works</div>
  <p class="footer-tagline">When you want the best for less<br>call velta rug works.</p>
  <div class="footer-phone">
    <svg viewBox="0 0 32 32"><circle cx="16" cy="16" r="14" fill="none" stroke="var(--yellow)" stroke-width="2.5"/><path d="M11 8l3 4-2 2c1 3 3 5 6 6l2-2 4 3-2 3c-7 0-13-6-13-13z" fill="var(--yellow)"/></svg>
    866-402-5719
  </div>
</section>

</body>
</html>
```